Design a flyer

Hi, I need a flyer designed for an electrical and air conditioning company based in brisbane, Australia.
We service the domestic market.
Flyer is to be double sided
Flyer size DL 210mm X 99mm
Was thinking one side services and discount coupons and the other side possible testimonials.
I have logo uploaded followed with the vehicle advertising, advertising stand alone sign and also business cards.
--------------------------
Coupon Cut out
save $150 OFF switchboard upgrades
save $150 Complimentary Electrical safety inspection
save $50 OFF Air Conditioner install or Service
save $50 next job if you leave feedback for first job
OVER $400 WORTH OF SAVINGS!
Our promise to you
* we will Arrive on time or we will pay you $100
* Before any job begins you will know the exact price
* We will leave your place as clean as we arrived
* if there is a problem and its our fault we will fix it for free
* provide a 12 month warranty on all parts
* we will provide friendly helpful service and advice
Phone number is 0487 562 903
Company Name - Quillbrook
License: 58164
ABN - 61 208 359 772
Also add swift pay, Orvane and Cindrel logo at the bottom
----------------------------
Here is what some of my customers have had to say
Extremely professional...
“Arrived when he said he would, sent through a written quote and was very reasonable. He also checked out our smoke
detectors whist he was here. He installed 2 ceiling fans and an air conditioner. He
cleaned up the mess and was very efficient. I will definitely use him again and recommend
him to family and friends”
P.M – Stretton
“Excellent service provider. He arrived on time with a call before arriving, than carried all jobs quickly and efficiently and left no mess at all. I will definitely recommend his service to others requiring an electrician. Thanks again!”
R.T – Greenslopes
“Over the long weekend, I had problems with my power, not only did you pick up the first phone call but you came out at 5am to fix it. Love the fact you’re a 24hr service!”
K.L – Mount Gravatt
---------------------------
NEW changes
Hi everyone,
Just want to say well done all the designers look great!
I will soon be choosing a winner, but there are a couple of changes i would like to make, if you revise you will be in for a win.
Instead of Save 50 if you leave feedback for the first job quote. I want to change that put $110 cross out and put $71.50 Install & Supply LED Downlights (min 20)
I want this to be the number one followed by switch board upgrade cut out.
Also $50 off air con install - don't put service.
And the third testimonial K.L Make sure it has a full stop
Also keep in mind. It is an electrical & air conditioning company.
Be creative with your design, don't want to see any pictures of people as they are not working for us at this time.
Remember key focus, on coupons, phone numbers, and website. Orvane and Plimtap can be small and out of the way same with the license numbers.
Thank you
Good Luck!
Domestic Market - Home owners
Air Conditioning

```html
<!DOCTYPE html>
<html lang="en">
<head>
<meta charset="utf-8">
<title>Quillbrook DL Flyer</title>
<link rel="stylesheet" href="https://fonts.googleapis.com/css2?family=Open+Sans:wght@400;600;700&family=Oswald:wght@400;500&display=swap">
<style>
:root{
  --stage:#4a4a4a;
  --paper:#ffffff;
  --ink:#1d1d1d;
  --brand-blue:#2a6db5;
  --brand-orange:#d8673a;
  --green:#9bbf2f;
  --salmon-light:#e9b6a2;
  --salmon:#e29c80;
  --blue:#3d86c6;
  --blue-light:#88b7de;
  --muted:#8a8a8a;
}
*{box-sizing:border-box;margin:0;padding:0}
html,body{width:1200px;height:800px;overflow:hidden}
body{background:var(--stage);font-family:"Open Sans",Arial,sans-serif;color:var(--ink);position:relative}
.flyer{position:absolute;width:340px;background:var(--paper);overflow:hidden}
.flyer--testimonials{left:250px;top:55px;height:705px}
.flyer--offers{left:662px;top:62px;height:696px}
.brand{position:absolute;top:56px;left:0;right:0;display:flex;justify-content:center;align-items:center;gap:8px}
.brand__name{font-size:36px;font-weight:400;color:var(--brand-blue);letter-spacing:.5px}
.brand__dot{width:12px;height:12px;border-radius:50%;background:var(--brand-orange)}
.section-title{position:absolute;left:22px;font-weight:400;text-transform:uppercase}
.testimonials-title{top:193px;font-size:19px;right:18px;display:flex;align-items:flex-end;gap:4px}
.testimonials-title::after{content:"";flex:1;border-bottom:1.5px dashed var(--green);margin-bottom:8px}
.divider{position:absolute;left:18px;right:18px;border-top:1.5px dashed var(--green)}
.bubble{position:absolute}
.quote{position:absolute;font-size:10px;line-height:1.32}
.quote p{margin-bottom:8px}
.quote cite{font-style:normal;font-size:11px}
.quote--one{top:234px;left:148px;width:176px}
.quote--one cite{display:block;padding-left:8px}
.quote--two{top:412px;left:22px;width:182px;text-align:right}
.quote--three{top:570px;left:155px;width:165px}
.phone-band{position:absolute;left:0;right:0;bottom:0;height:36px;background:var(--brand-orange);color:#fff;font-weight:700;font-size:17px;display:flex;align-items:center;justify-content:center}
.promise-title{top:156px;font-size:16px}
.promise-list{position:absolute;top:196px;left:22px;width:285px;list-style:none;font-size:11.5px;line-height:1.35}
.promise-list li{margin-bottom:6px;padding-left:10px;text-indent:-10px}
.promise-list li::before{content:"* "}
.phone-line{position:absolute;top:374px;left:22px;font-size:11px;font-weight:700}
.phone-line strong{font-size:17px}
.savings-title{position:absolute;top:421px;left:0;right:0;text-align:center;font-family:"Oswald",Arial,sans-serif;font-weight:400;font-size:25px;color:var(--green)}
.coupons{position:absolute;top:466px;left:0;width:340px;height:195px;display:grid;grid-template-columns:1fr 1fr;grid-template-rows:1fr 1fr}
.coupon{color:#fff;padding:12px 12px 0 24px;font-family:"Oswald",Arial,sans-serif;border:1.5px dashed rgba(255,255,255,.85);margin:-0.75px}
.coupon--switchboard{background:var(--salmon-light)}
.coupon--inspection{background:var(--salmon)}
.coupon--aircon{background:var(--blue)}
.coupon--feedback{background:var(--blue-light)}
.coupon__save{font-size:15px;line-height:1;font-weight:500}
.coupon__amount{font-size:34px;line-height:1.05;font-weight:500}
.coupon__note{font-family:"Open Sans",Arial,sans-serif;font-size:9px;line-height:1.15}
.footer{position:absolute;left:0;right:0;bottom:0;height:35px;display:flex;align-items:center;padding:0 16px;gap:12px}
.pay{display:flex;align-items:center;gap:4px;font-size:9px;font-weight:600;color:var(--muted)}
.pay__mark{width:9px;height:9px;background:var(--muted)}
.legal{margin-left:auto;text-align:right;font-size:7.5px;line-height:1.3;color:var(--muted)}
</style>
</head>
<body>

<article class="flyer flyer--testimonials">
  <div class="brand"><span class="brand__name">Quillbrook</span><span class="brand__dot"></span></div>
  <h2 class="section-title testimonials-title">Testimonials</h2>

  <svg class="bubble" style="top:232px;left:8px" width="132" height="130" viewBox="0 0 132 130" aria-hidden="true">
    <path d="M70 112 L98 128 L92 100 Z" fill="var(--green)"/>
    <circle cx="65" cy="62" r="52" fill="none" stroke="var(--green)" stroke-width="14"/>
  </svg>
  <div class="quote quote--one">
    <p>“Arrived when he said he would, sent through a written quote and was very reasonable. He also checked out our smoke detectors whist he was here. He installed 2 ceiling fans and an air conditioner. He cleaned up the mess and was very efficient. I will definitely use him again and recommend him to family and friends”</p>
    <cite>P.M – Stretton</cite>
  </div>

  <div class="divider" style="top:387px"></div>

  <svg class="bubble" style="top:398px;left:206px" width="112" height="118" viewBox="0 0 112 118" aria-hidden="true">
    <path d="M30 88 L12 116 L44 100 Z" fill="var(--green)"/>
    <circle cx="58" cy="56" r="46" fill="none" stroke="var(--green)" stroke-width="13"/>
  </svg>
  <div class="quote quote--two">
    <p>“Excellent service provider. He arrived on time with a call before arriving, than carried all jobs quickly and efficiently and left no mess at all. I will definitely recommend his service to others requiring an electrician. Thanks again!”</p>
    <cite>R.T – Greenslopes</cite>
  </div>

  <div class="divider" style="top:545px"></div>

  <svg class="bubble" style="top:556px;left:56px" width="96" height="96" viewBox="0 0 96 96" aria-hidden="true">
    <path d="M56 78 L86 92 L74 66 Z" fill="var(--green)"/>
    <circle cx="46" cy="44" r="37" fill="none" stroke="var(--green)" stroke-width="12"/>
  </svg>
  <div class="quote quote--three">
    <p>“Over the long weekend, I had problems with my power, not only did you pick up the first phone call but you came out at 5am to fix it. Love the fact you’re a 24hr service!”</p>
    <cite>K.L – Mount Gravatt</cite>
  </div>

  <div class="phone-band">Phone: 0487 562 903</div>
</article>

<article class="flyer flyer--offers">
  <div class="brand"><span class="brand__name">Quillbrook</span><span class="brand__dot"></span></div>
  <h2 class="section-title promise-title">OUR PROMISE TO YOU</h2>
  <ul class="promise-list">
    <li>we will Arrive on time or we will pay you $100</li>
    <li>Before any job begins you will know the exact price</li>
    <li>We will leave your place as clean as we arrived</li>
    <li>if there is a problem and its our fault we will fix it for free</li>
    <li>provide a 12 month warranty on all parts</li>
    <li>we will provide friendly helpful service and advice</li>
  </ul>
  <p class="phone-line">Phone number is <strong>0487 562 903</strong></p>

  <h2 class="savings-title">OVER $400 WORTH OF SAVINGS!</h2>
  <div class="coupons">
    <div class="coupon coupon--switchboard"><div class="coupon__save">SAVE</div><div class="coupon__amount">$150</div><div class="coupon__note">OFF switchboard upgrades</div></div>
    <div class="coupon coupon--inspection"><div class="coupon__save">SAVE</div><div class="coupon__amount">$150</div><div class="coupon__note">Complimentary Electrical safety inspection</div></div>
    <div class="coupon coupon--aircon"><div class="coupon__save">SAVE</div><div class="coupon__amount">$50</div><div class="coupon__note">OFF Air Conditioner install or Service</div></div>
    <div class="coupon coupon--feedback"><div class="coupon__save">SAVE</div><div class="coupon__amount">$50</div><div class="coupon__note">next job if you leave feedback for first job</div></div>
  </div>

  <footer class="footer">
    <span class="pay"><span class="pay__mark"></span>Orvane</span>
    <span class="pay"><span class="pay__mark"></span>Plimtap</span>
    <span class="pay"><span class="pay__mark"></span>Cindrel</span>
    <div class="legal">License: 58164<br>ABN - 61 208 359 772</div>
  </footer>
</article>

</body>
</html>
```